KerrLow Farm

Need a nice simple clean double sided business card that has our logo and info on:
Kerr Low Farm
Martin & Felicity Kerr Low
kerrlowfarm@mailbarn.example
Martin: 1-780-555-0148
Felicity: 1-780-555-0193
Instagram @ kerrlow_farm

Contact Information for Business Card

Martin & Felicity Kerr Low kerrlowfarm@mailbarn.example Martin: 1-780-555-0148 Felicity: 1-780-555-0193

```html
<!DOCTYPE html>
<html lang="en">
<head>
<meta charset="utf-8">
<title>Kerr Low Farm – Business Card</title>
<link rel="stylesheet" href="https://fonts.googleapis.com/css2?family=Cinzel:wght@500&family=Open+Sans:wght@400&display=swap">
<style>
  :root {
    --backdrop: #5f5f5f;
    --card: #ffffff;
    --farm-green: #6ba322;
    --wheat-gold: #f2a933;
    --field-top: rgba(255, 255, 255, 0);
    --field-bottom: #fbedd6;
  }
  * { box-sizing: border-box; margin: 0; padding: 0; }
  html, body {
    width: 885px;
    height: 1200px;
    overflow: hidden;
    background: var(--backdrop);
  }
  .sheet {
    position: relative;
    width: 885px;
    height: 1200px;
  }
  .card {
    position: absolute;
    left: 29px;
    width: 809px;
    height: 535px;
    background: var(--card);
    border-radius: 40px;
    overflow: hidden;
  }
  .card--front { top: 34px; }
  .card--back  { top: 631px; }

  .wheat-field {
    position: absolute;
    left: 0;
    right: 0;
    bottom: 0;
    height: 235px;
    background: linear-gradient(180deg, var(--field-top) 0%, var(--field-bottom) 100%);
  }
  .card--back .wheat-field { height: 260px; }

  .brand {
    position: absolute;
    left: 0;
    right: 0;
    text-align: center;
  }
  .brand__ring {
    display: block;
    margin: 0 auto;
  }
  .brand__name {
    display: block;
    margin-top: 6px;
    font-family: "Cinzel", Georgia, serif;
    font-weight: 500;
    font-size: 44px;
    line-height: 1.1;
    letter-spacing: 0.5px;
    color: var(--farm-green);
    text-transform: uppercase;
  }
  .card--front .brand { top: 76px; }
  .card--back .brand  { top: 183px; }

  .contact {
    position: absolute;
    left: 0;
    right: 28px;
    top: 376px;
    text-align: center;
    font-family: "Open Sans", Arial, sans-serif;
    font-size: 21px;
    line-height: 30px;
    color: var(--wheat-gold);
    list-style: none;
  }
</style>
</head>
<body>
<main class="sheet">

  <section class="card card--front" aria-label="Business card front">
    <div class="wheat-field" role="img" aria-label="Blurred wheat field photograph"></div>
    <div class="brand">
      <svg class="brand__ring" width="148" height="148" viewBox="0 0 148 148" aria-hidden="true">
        <circle cx="74" cy="74" r="70" fill="none" stroke="var(--farm-green)" stroke-width="5"/>
      </svg>
      <span class="brand__name">Kerr Low Farm</span>
    </div>
    <ul class="contact">
      <li>kerrlowfarm@mailbarn.example</li>
      <li>Martin: 1-780-555-0148 Felicity: 1-780-555-0193</li>
      <li>Instagram @ kerrlow_farm</li>
    </ul>
  </section>

  <section class="card card--back" aria-label="Business card back">
    <div class="wheat-field" role="img" aria-label="Blurred wheat field photograph"></div>
    <div class="brand">
      <svg class="brand__ring" width="146" height="146" viewBox="0 0 146 146" aria-hidden="true">
        <circle cx="73" cy="73" r="69" fill="none" stroke="var(--farm-green)" stroke-width="5"/>
      </svg>
      <span class="brand__name">Kerr Low Farm</span>
    </div>
  </section>

</main>
</body>
</html>
```